Business Card Design Project

We require business cards to be produced with the following design
http://files.brieflanter.net/art_img/38217/49302/49302_5520914_38217_image.jpg
Rather than lantern yard, please use Dolvane as the comapny name.
Please also use the following contact details:
1.
Peter Halloway
Entrepreneur
07923418870
phalloway@dolvane.net
2.
Tom Brenner
Founder
07844512039
tbrenner@dolvane.net
Please add:
Friendpage favicion facebook.com/dolvane
Linkwork favicon linkedin/peterhalloway
Callwave favicon phalloway
Linkwork favicon linkedin/thomasbrenner
Callwave favicon thomasbrenner
Circleplus favicon tombrenner@maildrop.net
To the back
Industry/Entity Type
Business
Look and feel
Each slider illustrates characteristics of the customer's brand and the style your logo design should communicate.

```html
<!DOCTYPE html>
<html lang="en">
<head>
<meta charset="utf-8">
<title>Dolvane – Business Card</title>
<link href="https://fonts.googleapis.com/css2?family=Roboto+Condensed:wght@400;700&display=swap" rel="stylesheet">
<style>
  :root {
    --page-bg: #f2f2f2;
    --card-black: #050505;
    --accent-red: #c40000;
    --band-red-top: #b30000;
    --band-red-bottom: #6e0000;
    --text-white: #ffffff;
    --text-dark: #111111;
  }
  * { box-sizing: border-box; margin: 0; padding: 0; }
  html, body {
    width: 1200px;
    height: 686px;
    overflow: hidden;
    background: var(--page-bg);
  }
  .canvas {
    position: relative;
    width: 1200px;
    height: 686px;
  }
  .business-card {
    position: absolute;
    left: 100px;
    top: 73px;
    width: 1000px;
    height: 540px;
    background: var(--card-black);
    overflow: hidden;
    box-shadow: 0 10px 30px rgba(0, 0, 0, 0.25);
    font-family: "Roboto Condensed", "Arial Narrow", sans-serif;
  }
  .brand {
    position: absolute;
    left: 70px;
    top: 222px;
    display: flex;
    align-items: center;
    gap: 22px;
  }
  .brand-square {
    width: 66px;
    height: 66px;
    background: var(--accent-red);
  }
  .brand-name {
    color: var(--text-white);
    font-weight: 700;
    font-size: 92px;
    line-height: 1;
    letter-spacing: 1px;
  }
  .divider {
    position: absolute;
    left: 560px;
    top: 60px;
    width: 5px;
    height: 330px;
    background: var(--accent-red);
    border-radius: 3px;
  }
  .social-list {
    position: absolute;
    left: 580px;
    width: 400px;
    list-style: none;
    text-align: center;
    color: var(--text-white);
    font-weight: 700;
    font-size: 21px;
    line-height: 30px;
    white-space: nowrap;
  }
  .social-list--first { top: 62px; }
  .social-list--second { top: 212px; }
  .contact-band {
    position: absolute;
    left: 0;
    bottom: 0;
    width: 100%;
    height: 112px;
    background: linear-gradient(to bottom, var(--band-red-top), var(--band-red-bottom));
    display: flex;
    align-items: center;
    justify-content: center;
    gap: 34px;
    color: var(--text-dark);
    font-weight: 700;
    font-size: 30px;
    letter-spacing: 3px;
    white-space: nowrap;
  }
</style>
</head>
<body>
  <div class="canvas">
    <section class="business-card">
      <div class="brand">
        <span class="brand-square"></span>
        <span class="brand-name">DOLVANE</span>
      </div>

      <span class="divider"></span>

      <ul class="social-list social-list--first">
        <li>Friendpage favicion friendpage.com/dolvane</li>
        <li>Linkwork favicon linkwork/peterhalloway</li>
        <li>Callwave favicon peterhalloway</li>
        <li>Circleplus favicon phalloways@maildrop.net</li>
      </ul>

      <ul class="social-list social-list--second">
        <li>Friendpage favicion friendpage.com/dolvane</li>
        <li>Linkwork favicon linkwork/thomasbrenner</li>
        <li>Callwave favicon thomasbrenner</li>
        <li>Circleplus favicon tombrenner@maildrop.net</li>
      </ul>

      <div class="contact-band">
        <span class="contact-name">Tom Brenner</span>
        <span class="contact-role">Founder</span>
        <span class="contact-phone">07844512039</span>
        <span class="contact-email">tbrenner@dolvane.net</span>
      </div>
    </section>
  </div>
</body>
</html>
```